high-impact, conversion-focused website redesign for the government sector

Objective: To design and develop a high-impact, conversion-focused digital platform that solidifies Harrowgate Lumen Advisors (HLA) as the leading communications and strategy firm for government, defense, and industrial clients. The site must project authority, innovation, and sophisticated precision. See the creative breif for more information

Target Market(s)

Government contractors

Industry/Entity Type

Government, defense, industrials

Coding

Coded - Design and coding required

Number of Pages Required

5+ page

Font styles to use
Other font styles liked:
• See the current website

Requirements
Must have
• See design brief
Nice to have
• See design brief
Should not have
• See design brief

```html
<!DOCTYPE html>
<html lang="en">
<head>
<meta charset="utf-8">
<title>Harrowgate Lumen Advisors — Accelerate Your Mission</title>
<link rel="stylesheet" href="https://fonts.googleapis.com/css2?family=Audiowide&family=Montserrat:wght@400;500;600;700&display=swap">
<style>
:root{
  --navy:#06101f;
  --navy-2:#0a1a30;
  --panel:#0d1f38;
  --green:#6cc22b;
  --blue:#1e8fe6;
  --blue-deep:#0b66b8;
  --orange:#f7941d;
  --white:#ffffff;
  --muted:#a9b6c8;
  --ink:#1b2433;
  --grey:#6b7380;
}
*{box-sizing:border-box;margin:0;padding:0}
html,body{width:1200px;height:4955px;overflow:hidden}
body{background:var(--navy);color:var(--white);font-family:"Montserrat",sans-serif;position:relative}
.display{font-family:"Audiowide",sans-serif;font-weight:400;text-transform:uppercase;letter-spacing:1px}
.accent-blue{color:var(--blue)}
section,footer{position:absolute;left:0;width:1200px}
.abs{position:absolute}

/* buttons */
.btn{position:absolute;display:flex;align-items:center;height:30px;background:var(--white);color:var(--ink);font-size:12px;font-weight:500;padding-left:16px;text-decoration:none;white-space:nowrap}
.btn .chev{position:absolute;right:-14px;top:-1px}

/* brand */
.brand{font-weight:600;color:var(--white);letter-spacing:1.5px;text-align:center;line-height:1.25;font-size:14px;white-space:nowrap}
.brand-dot{width:22px;height:22px;border-radius:50%;background:var(--blue);margin:0 auto 6px}

/* hero */
.hero{top:0;height:673px;background:
  radial-gradient(ellipse 360px 300px at 600px 250px,#2d5f9a 0%,#12325a 45%,transparent 75%),
  radial-gradient(ellipse 700px 500px at 600px 300px,#0c1e36 0%,#050b16 80%);}
.nav a{position:absolute;top:28px;color:var(--white);font-size:12px;text-decoration:none}
.hero-title-1{position:absolute;top:282px;width:1200px;text-align:center;font-size:53px;color:var(--green);text-shadow:0 0 18px rgba(108,194,43,.5)}
.hero-title-2{position:absolute;top:340px;width:1200px;text-align:center;font-size:80px;color:var(--white)}
.hero p{position:absolute;top:452px;left:280px;width:640px;text-align:center;font-size:12.5px;line-height:23px}
.slider-arrow{position:absolute;top:484px;width:26px;height:26px;border:1px solid rgba(255,255,255,.6);display:flex;align-items:center;justify-content:center}

/* results */
.results{top:673px;height:790px;background:linear-gradient(180deg,#07152a 0%,#0a1d36 55%,#07152a 100%)}
.section-title{position:absolute;width:1200px;text-align:center;font-size:27px;line-height:37px}
.section-sub{position:absolute;width:1200px;text-align:center;font-size:12px;color:var(--muted);line-height:19px}
.stat{position:absolute;top:229px;width:272px;height:160px;border:1px solid var(--green);background:rgba(6,16,31,.55);text-align:center}
.stat .num{font-family:"Audiowide",sans-serif;font-size:46px;color:var(--green);margin-top:22px}
.stat .lbl{font-size:11px;color:var(--muted);line-height:16px;margin-top:10px}
.stat .lbl b{color:var(--white);font-weight:600}
.stat .tip{position:absolute;left:124px;bottom:0;border-left:12px solid transparent;border-right:12px solid transparent;border-bottom:12px solid var(--green)}
.quote{position:absolute;top:538px;width:294px;height:154px;background:var(--panel);text-align:center;padding:24px 22px 0}
.quote.featured{background:var(--blue-deep)}
.quote h3{font-size:13px;font-weight:600;line-height:19px}
.quote p{font-size:9px;line-height:14px;color:#c9d4e3;margin-top:10px}
.quote .mark{position:absolute;right:12px;top:-2px;font-family:"Audiowide",sans-serif;font-size:34px;color:#6c7a90}
.dots{position:absolute;top:731px;left:568px;display:flex;gap:6px;align-items:center}
.dots i{display:block;height:3px;width:8px;background:#7d8aa0}
.dots i.on{width:36px;background:var(--white)}

/* services */
.services{top:1463px;height:712px;background:linear-gradient(180deg,#07152a,#050b16)}
.svc{position:absolute;width:231px;height:230px;background:var(--white);color:var(--ink);text-align:center;padding-top:14px}
.svc .n{font-size:11px;color:var(--grey)}
.svc .hex{margin:6px auto 0;display:block}
.svc h4{font-size:13px;font-weight:600;margin-top:10px;white-space:nowrap}
.svc .rule{width:32px;height:2px;background:var(--green);margin:9px auto 0}
.svc p{font-size:9px;line-height:14px;color:var(--grey);padding:0 18px;margin-top:10px}
.svc .go{position:absolute;right:0;bottom:0;width:26px;height:26px;background:#8a93a0;display:flex;align-items:center;justify-content:center}
.svc.active .n,.svc.active h4{color:var(--green)}
.svc.active .go{background:var(--green)}

/* strategic */
.strategic{top:2175px;height:335px;background:linear-gradient(90deg,#0a2847 0%,#0d3358 50%,#0a2440 100%)}
.strategic h2{position:absolute;left:565px;top:50px;width:540px;font-size:24px;line-height:37px}
.strategic p{position:absolute;left:565px;top:136px;width:510px;font-size:9.5px;line-height:15px;color:#d5dfec}

/* edge */
.edge{top:2510px;height:452px;background:linear-gradient(180deg,#050b16,#081628)}
.edge h2{position:absolute;left:125px;top:56px;font-size:27px}
.edge .lead{position:absolute;left:125px;top:100px;width:300px;font-size:11.5px;line-height:18px;color:#d8e1ee}
.edge .bar{position:absolute;left:125px;top:146px;width:38px;height:2px;background:var(--blue)}
.edge .body{position:absolute;left:125px;top:165px;width:390px;font-size:11px;line-height:21px;color:#d8e1ee}
.edge .frame{position:absolute;left:546px;top:75px;width:533px;height:324px;background:var(--green)}
.edge .photo{position:absolute;left:552px;top:63px;width:527px;height:324px;border:3px solid var(--white);background:linear-gradient(135deg,#1c3a55 0%,#0e2236 45%,#4a6f8c 100%)}

/* insights */
.insights{top:2962px;height:653px;background:linear-gradient(180deg,#081628,#0a1c33 70%,#061022)}
.post{position:absolute;overflow:hidden}
.post .tag{position:absolute;left:0;top:0;background:var(--white);color:var(--blue);font-size:10.5px;padding:3px 10px}
.post h4{position:absolute;font-size:13px;font-weight:500;line-height:20px}
.post .watch{position:absolute;background:var(--white);color:var(--ink);font-size:12px;padding:7px 12px}

/* expect */
.expect{top:3615px;height:640px;background:linear-gradient(180deg,#061022,#050b16)}
.expect .wheel{position:absolute;left:144px;top:106px;width:414px;height:424px;background:linear-gradient(135deg,#6cc22b 0%,#1e8fe6 50%,#f7941d 100%);opacity:.85}
.expect h2{position:absolute;left:598px;top:73px;font-size:27px;line-height:37px}
.expect .intro{position:absolute;left:598px;top:155px;width:470px;font-size:11px;line-height:18px;color:#cdd7e4}
.expect .body{position:absolute;left:598px;width:480px;font-size:11px;line-height:20px;color:#dbe3ee}
.expect .body b{color:var(--white);font-weight:600}

/* cta */
.cta-wrap{top:4255px;height:400px;background:var(--navy)}
.cta{position:absolute;left:125px;top:18px;width:950px;height:286px;border:2px solid #3aa0ff;background:radial-gradient(ellipse 420px 220px at 475px 130px,#1c73c8 0%,#0f4d95 55%,#0a376f 100%);text-align:center}
.cta h2{font-size:27px;line-height:38px;margin-top:70px}
.cta p{font-size:12px;line-height:19px;margin-top:10px}
.ghost{position:absolute;left:0;top:305px;width:1200px;text-align:center;font-family:"Audiowide",sans-serif;font-size:90px;color:rgba(255,255,255,.06);white-space:nowrap;letter-spacing:4px}

/* footer */
.footer{top:4655px;height:300px;background:#050b16}
.footer .about{position:absolute;left:125px;top:178px;width:240px;font-size:9px;line-height:14px;color:#c5cfdc}
.footer .badge{position:absolute;top:240px;width:38px;height:22px;background:#e9edf2}
.footer .col-line{position:absolute;top:0;width:1px;height:255px;background:rgba(255,255,255,.12)}
.footer h5{position:absolute;top:40px;font-size:12px;font-weight:600}
.footer ul{position:absolute;top:80px;list-style:none;font-size:9px;line-height:16px;color:#d8e1ee}
.footer ul li.current{color:var(--green)}
.footer .contact{position:absolute;left:895px;font-size:9px;line-height:14px}
.footer .legal{position:absolute;left:0;top:270px;width:1200px;height:30px;border-top:1px solid rgba(255,255,255,.12);text-align:center;font-size:10.5px;line-height:30px;color:#d8e1ee}
</style>
</head>
<body>

<section class="hero">
  <div class="abs" role="img" aria-label="View of Earth from a spacecraft window" style="left:0;top:0;width:1200px;height:673px"></div>
  <nav class="nav">
    <a style="left:183px">Advisory Services</a>
    <a style="left:341px">About Us</a>
    <a style="left:805px">Blog</a>
    <a style="left:888px">Contact Us</a>
  </nav>
  <div class="abs" style="left:480px;top:14px;width:240px">
    <div class="brand-dot"></div>
    <div class="brand">HARROWGATE LUMEN<br>ADVISORS</div>
  </div>
  <h1 class="hero-title-1 display">Accelerate</h1>
  <div class="hero-title-2 display">Your Mission</div>
  <p>Harrowgate Lumen Advisors exists for one reason to help connect the federal ecosystem with the technologies that matter most to America and her allies. We help build the communications, government affairs and marketing strategies and systems your organization needs to grow and protect market share –helping our clients meet their mission objectives.</p>
  <div class="slider-arrow" style="left:125px"><svg width="8" height="10"><path d="M6 1 2 5l4 4" stroke="#fff" fill="none" stroke-width="1.5"/></svg></div>
  <div class="slider-arrow" style="left:1048px"><svg width="8" height="10"><path d="M2 1l4 4-4 4" stroke="#fff" fill="none" stroke-width="1.5"/></svg></div>
  <a class="btn" style="left:484px;top:566px;width:214px">View Our Advisory Services
    <svg class="chev" width="32" height="32"><path d="M0 0h14l16 16-16 16H0l16-16z" fill="var(--blue)"/><path d="M8 4h6l12 12-12 12H8l12-12z" fill="var(--green)"/></svg></a>
</section>

<section class="results">
  <h2 class="section-title display" style="top:78px">Proven Results That Drive<br>Real <span class="accent-blue">Growth</span></h2>
  <p class="section-sub" style="top:155px">We’ve helped brands strengthen their digital presence, expand their network, and accelerate opportunities<br>across the defense, space, and government sectors. In just one year, our clients have achieved :</p>
  <div class="stat" style="left:131px"><div class="num">+72%</div><div class="lbl">Increase in database contacts via<br><b>CRM + targeted</b> campaigns</div><span class="tip"></span></div>
  <div class="stat" style="left:456px"><div class="num">100+</div><div class="lbl">Introductions to <b>tech-scouting contracts</b><br>across DoD and aerospace/defense</div><span class="tip"></span></div>
  <div class="stat" style="left:781px"><div class="num">570%</div><div class="lbl">stock growth / <b>$50M AUD</b> in new<br>investment for a rapidly scaling client</div><span class="tip"></span></div>

  <h2 class="section-title display" style="top:462px">Our <span class="accent-blue">Client</span> Quotes</h2>
  <div class="quote" style="left:125px"><span class="mark">❞</span><h3>-Brackwell Associates Account Lead</h3><p>“Collaborating with Harrowgate Lumen Advisors was a game-changer; their innovative approach and strategic insight propelled our work to new heights. Their unwavering commitment to not just meeting, but exceeding expectations, has been a cornerstone of our success.”</p></div>
  <div class="quote featured" style="left:454px"><h3>Dana Holloway, President and<br>Managing Director</h3><p>Partnering with Harrowgate Lumen Advisors accelerated the growth of our company. Their strategic insight, deep federal expertise, and hands-on support transformed our U.S. expansion. In less than six months…</p></div>
  <div class="quote" style="left:781px"><span class="mark">❞</span><h3>Renee Castor, Vice President<br>of Customer</h3><p>“Partnering with Harrowgate Lumen for our speaker acquisition and management helped to make Meridian Works Vanguard Summit 2023 a major success. We sold out three weeks before our event…</p></div>
  <div class="dots"><i></i><i class="on"></i><i></i></div>
</section>

<section class="services">
  <h2 class="section-title display" style="top:65px">Our Advisory <span class="accent-blue">Services</span></h2>
  <p class="section-sub" style="top:108px">Strategic support to strengthen your position across the federal ecosystem.</p>

  <div class="svc" style="left:125px;top:156px"><div class="n">01</div><svg class="hex" width="40" height="44"><path d="M20 2 38 12v20L20 42 2 32V12z" fill="none" stroke="#2b3442" stroke-width="1.5"/><rect x="13" y="17" width="14" height="10" fill="none" stroke="#2b3442" stroke-width="1.4"/></svg><h4>Corporate Communications</h4><div class="rule"></div><p>Clear, compelling messaging that defines your mission, sharpens your narrative, and aligns your organization internally and externally.</p><span class="go"><svg width="10" height="10"><path d="M2 8 8 2M3 2h5v5" stroke="#fff" fill="none" stroke-width="1.4"/></svg></span></div>
  <div class="svc active" style="left:365px;top:156px"><div class="n">02</div><svg class="hex" width="40" height="44"><path d="M20 2 38 12v20L20 42 2 32V12z" fill="var(--green)"/><path d="M12 19h5l9-5v16l-9-5h-5z" fill="#fff"/></svg><h4>Public Relations</h4><div class="rule"></div><p>Media engagement, press strategy, and thought-leadership campaigns that elevate your voice in the defense, technology, and government markets.</p><span class="go"><svg width="10" height="10"><path d="M2 8 8 2M3 2h5v5" stroke="#fff" fill="none" stroke-width="1.4"/></svg></span></div>
  <div class="svc" style="left:604px;top:156px"><div class="n">03</div><svg class="hex" width="40" height="44"><path d="M20 2 38 12v20L20 42 2 32V12z" fill="none" stroke="#2b3442" stroke-width="1.5"/><circle cx="20" cy="16" r="3" fill="none" stroke="#2b3442" stroke-width="1.4"/><circle cx="13" cy="28" r="3" fill="none" stroke="#2b3442" stroke-width="1.4"/><circle cx="27" cy="28" r="3" fill="none" stroke="#2b3442" stroke-width="1.4"/></svg><h4>Government Affairs</h4><div class="rule"></div><p>Strategic guidance and relationship-building to help you navigate policy environments, engage federal stakeholders, and advance mission-aligned objectives.</p><span class="go"><svg width="10" height="10"><path d="M2 8 8 2M3 2h5v5" stroke="#fff" fill="none" stroke-width="1.4"/></svg></span></div>
  <div class="svc" style="left:844px;top:156px"><div class="n">04</div><svg class="hex" width="40" height="44"><path d="M20 2 38 12v20L20 42 2 32V12z" fill="none" stroke="#2b3442" stroke-width="1.5"/><circle cx="20" cy="22" r="4" fill="none" stroke="#2b3442" stroke-width="1.4"/><path d="M20 13v4M20 27v4M11 22h4M25 22h4" stroke="#2b3442" stroke-width="1.4"/></svg><h4>Crisis Communications</h4><div class="rule"></div><p>Rapid, precise, and disciplined communication support to protect your reputation and manage high-risk moments with confidence.</p><span class="go"><svg width="10" height="10"><path d="M2 8 8 2M3 2h5v5" stroke="#fff" fill="none" stroke-width="1.4"/></svg></span></div>

  <div class="svc" style="left:125px;top:420px"><div class="n">05</div><svg class="hex" width="40" height="44"><path d="M20 2 38 12v20L20 42 2 32V12z" fill="none" stroke="#2b3442" stroke-width="1.5"/><rect x="14" y="14" width="12" height="16" fill="none" stroke="#2b3442" stroke-width="1.4"/></svg><h4>Digital Marketing</h4><div class="rule"></div><p>Targeted campaigns, CRM systems, analytics, and online strategy to strengthen your digital footprint and accelerate growth opportunities.</p><span class="go"><svg width="10" height="10"><path d="M2 8 8 2M3 2h5v5" stroke="#fff" fill="none" stroke-width="1.4"/></svg></span></div>
  <div class="svc" style="left:365px;top:420px"><div class="n">06</div><svg class="hex" width="40" height="44"><path d="M20 2 38 12v20L20 42 2 32V12z" fill="none" stroke="#2b3442" stroke-width="1.5"/><path d="M13 30V18M20 30V14M27 30V22" stroke="#2b3442" stroke-width="1.8"/></svg><h4>Strategic Connections</h4><div class="rule"></div><p>Direct access to a powerful network across DoD, federal agencies, industry leaders, investors, and innovators to open doors and expand opportunities.</p><span class="go"><svg width="10" height="10"><path d="M2 8 8 2M3 2h5v5" stroke="#fff" fill="none" stroke-width="1.4"/></svg></span></div>
  <div class="svc" style="left:604px;top:420px"><div class="n">07</div><svg class="hex" width="40" height="44"><path d="M20 2 38 12v20L20 42 2 32V12z" fill="none" stroke="#2b3442" stroke-width="1.5"/><circle cx="20" cy="17" r="4" fill="none" stroke="#2b3442" stroke-width="1.4"/><path d="M12 30c1-5 4-7 8-7s7 2 8 7" fill="none" stroke="#2b3442" stroke-width="1.4"/></svg><h4>Investor Relations</h4><div class="rule"></div><p>Messaging, positioning, and communications that support fundraising, valuation increases, market transitions, and investor confidence.</p><span class="go"><svg width="10" height="10"><path d="M2 8 8 2M3 2h5v5" stroke="#fff" fill="none" stroke-width="1.4"/></svg></span></div>
  <div class="svc" style="left:844px;top:420px"><div class="n">08</div><svg class="hex" width="40" height="44"><path d="M20 2 38 12v20L20 42 2 32V12z" fill="none" stroke="#2b3442" stroke-width="1.5"/><rect x="12" y="15" width="16" height="14" fill="none" stroke="#2b3442" stroke-width="1.4"/><path d="M12 19h16" stroke="#2b3442" stroke-width="1.4"/></svg><h4>Event Management</h4><div class="rule"></div><p>End-to-end planning, speaker acquisition, logistics, and promotional strategy for high-impact events in the federal and defense innovation ecosystem.</p><span class="go"><svg width="10" height="10"><path d="M2 8 8 2M3 2h5v5" stroke="#fff" fill="none" stroke-width="1.4"/></svg></span></div>
</section>

<section class="strategic">
  <div class="abs" role="img" aria-label="Advisor working at a desk in a dim office" style="left:480px;top:0;width:720px;height:335px;background:linear-gradient(90deg,rgba(10,40,71,0),rgba(30,70,110,.35) 40%,rgba(10,36,64,0))"></div>
  <div class="abs" role="img" aria-label="Astronaut in a spacecraft corridor" style="left:125px;top:0;width:342px;height:335px;background:linear-gradient(135deg,#1a5a8c 0%,#2c6f6a 50%,#3c7a2e 100%)"></div>
  <h2 class="display">Strategic Advisors for High-<br>Stakes Environments</h2>
  <p>Harrowgate Lumen Advisors is a mission-driven advisory firm supporting innovators across defense, aerospace, national security, and federal technology. With a team of former military leaders, federal communicators, and industry strategists, we help organizations build the communications, government affairs, and marketing systems needed to grow in complex federal environments. Our deep sector insight and powerful network drive measurable outcomes that strengthen positioning, accelerate opportunity, and support mission success.</p>
  <a class="btn" style="left:565px;top:239px;width:164px">Learn About Us
    <svg class="chev" width="32" height="32"><path d="M0 0h14l16 16-16 16H0l16-16z" fill="var(--blue)"/><path d="M8 4h6l12 12-12 12H8l12-12z" fill="var(--green)"/></svg></a>
</section>

<section class="edge">
  <h2 class="display">Our <span class="accent-blue">Edge</span></h2>
  <p class="lead">A strategic edge shaped by decades inside the federal ecosystem.</p>
  <span class="bar"></span>
  <div class="body">
    <p style="margin-top:6px">We combine deep federal sector insight, technical understanding, and a powerful network across government, industry, investors, and media. Our proven approach drives results — from major contract wins and successful M&amp;A to increased valuation, strategic investment, and political support.</p>
    <p>Our strategies begin with your mission and business goals, ensuring every message, relationship, and action advances growth and impact.</p>
  </div>
  <a class="btn" style="left:125px;top:365px;width:164px">Explore Our EDGE
    <svg class="chev" width="32" height="32"><path d="M0 0h14l16 16-16 16H0l16-16z" fill="var(--blue)"/><path d="M8 4h6l12 12-12 12H8l12-12z" fill="var(--green)"/></svg></a>
  <div class="frame" style="left:546px;top:75px;width:200px;height:324px"></div>
  <div class="photo" role="img" aria-label="Operations center with screens showing maps and data"></div>
</section>

<section class="insights">
  <h2 class="section-title display" style="top:76px">Insights from the Federal<br><span class="accent-blue">Innovation</span> Frontline</h2>
  <p class="section-sub" style="top:151px">Our blog covers emerging technologies, policy shifts, industry trends, and practical<br>strategies to help organizations thrive in the federal ecosystem.</p>

  <div class="post" style="left:125px;top:207px;width:519px;height:323px;background:linear-gradient(180deg,#2a3a4c 0%,#1a2633 50%,#3f8a2a 55%,#4d9a2d 100%)" role="img" aria-label="Laptop displaying a drone interface">
    <span class="tag">Defense Tech</span>
    <h4 style="left:25px;top:196px;width:340px">How Dual-Use Technology Is Transforming the Defense Innovation Pipeline</h4>
    <p class="abs" style="left:25px;top:246px;width:330px;font-size:9px;line-height:13px;color:#e6f2dc">Emerging dual-use technologies are reshaping how the DoD evaluates, procures, and deploys new capabilities. This article breaks down the trends shaping 2025—and what innovators must understand to stay ahead of shifting defense priorities.</p>
    <span class="watch" style="left:395px;top:268px">Watch Now</span>
  </div>
  <div class="post" style="left:656px;top:207px;width:419px;height:162px;background:linear-gradient(180deg,#3b6f9c 0%,#1f3f63 60%,#12253e 100%)" role="img" aria-label="City skyline at dusk">
    <span class="tag">Policy &amp; Government Affairs</span>
    <h4 style="left:12px;top:96px;width:290px">Navigating Federal Policy Shifts: What Contractors Need to Know Now</h4>
    <span class="watch" style="left:310px;top:100px">Watch Now</span>
  </div>
  <div class="post" style="left:656px;top:376px;width:419px;height:154px;background:linear-gradient(180deg,#6e8196 0%,#37495d 55%,#1d2a3a 100%)" role="img" aria-label="Hand touching a tablet screen">
    <span class="tag">GovComms &amp; Strategy</span>
    <h4 style="left:12px;top:92px;width:290px">Building a Federal Communications Strategy That Cuts Through the Noise</h4>
    <span class="watch" style="left:310px;top:92px">Watch Now</span>
  </div>
  <a class="btn" style="left:511px;top:563px;width:164px">View All Blogs
    <svg class="chev" width="32" height="32"><path d="M0 0h14l16 16-16 16H0l16-16z" fill="var(--blue)"/><path d="M8 4h6l12 12-12 12H8l12-12z" fill="var(--green)"/></svg></a>
</section>

<section class="expect">
  <div class="wheel" role="img" aria-label="Partnership process graphic showing the service areas around the brand"></div>
  <h2 class="display">What to Expect When<br><span class="accent-blue">Partnering</span> With Us</h2>
  <p class="intro">Our structured approach ensures every engagement begins with insight, aligns with your mission, and delivers results.</p>
  <p class="body" style="top:209px">With decades of experience, a <b>results-focused methodology</b>, and cutting-edge marketing and communications tools and technologies, we begin every engagement with a discovery and planning process to ensure we are building a strategy that cuts through the noise to achieve our measurable results. As specialists in government crisis communications, we additionally examine our client’s current strategy for risks ensuring we are building on a stable foundation.</p>
  <p class="body" style="top:350px">By truly understanding our client’s goals, <b>key milestones, potential areas of risk, ideal customer</b> and <b>investor targets, partner profiles</b>, and other key drivers, we create messaging and strategy that goes beyond traditional brand awareness to meet mission objectives. As a full service firm, we work across all the areas in the graphic.</p>
  <p class="body" style="top:469px"><b>Our time-tested methodology</b> is based on building and executing a strategy aligned with client mission objectives. With the strategy in place, we execute tactics with precision, efficiency, and the highest quality of customer service.</p>
  <a class="btn" style="left:598px;top:562px;width:164px;padding-left:34px">Get In Touch
    <svg class="chev" width="32" height="32"><path d="M0 0h14l16 16-16 16H0l16-16z" fill="var(--blue)"/><path d="M8 4h6l12 12-12 12H8l12-12z" fill="var(--green)"/></svg></a>
</section>

<section class="cta-wrap">
  <div class="ghost">HARROWGATE LUMEN</div>
  <div class="cta">
    <h2 class="display">Ready to Accelerate<br>Your Mission?</h2>
    <p>Let’s build the strategy, connections, and communications systems<br>that move your organization forward.</p>
    <a class="btn" style="left:361px;top:198px;width:214px">Request More Information
      <svg class="chev" width="32" height="32"><path d="M0 0h14l16 16-16 16H0l16-16z" fill="var(--blue)"/><path d="M8 4h6l12 12-12 12H8l12-12z" fill="var(--green)"/></svg></a>
  </div>
</section>

<footer class="footer">
  <div class="abs" style="left:125px;top:30px;width:230px">
    <div class="brand-dot" style="margin:0 0 6px 0"></div>
    <div class="brand" style="text-align:left;font-size:14px">HARROWGATE LUMEN<br>ADVISORS</div>
  </div>
  <p class="about">Harrowgate Lumen Advisors provides strategic communications and government affairs support for organizations operating in the federal ecosystem.</p>
  <span class="badge" style="left:125px"></span>
  <span class="badge" style="left:170px;border-radius:50%;width:22px"></span>
  <span class="badge" style="left:200px"></span>
  <span class="badge" style="left:245px"></span>

  <span class="col-line" style="left:438px"></span>
  <span class="col-line" style="left:615px"></span>
  <span class="col-line" style="left:848px"></span>

  <h5 style="left:487px">Quick Links</h5>
  <ul style="left:487px"><li class="current">Home</li><li>Advisory Services</li><li>About Us</li><li>Blog</li><li>Contact Us</li></ul>

  <h5 style="left:664px">Our Services</h5>
  <ul style="left:664px"><li>Corporate Communications</li><li>Public Relations</li><li>Government Affairs (NEW)</li><li>Crisis Communications (NEW)</li><li>Digital Marketing</li><li>Strategic Connections (NEW)</li><li>Investor Relations</li><li>Event Management</li></ul>

  <h5 style="left:895px">Contact Us</h5>
  <div class="contact" style="top:82px;display:flex;gap:8px;align-items:center">
    <svg width="16" height="16"><circle cx="8" cy="8" r="8" fill="var(--green)"/><rect x="4" y="5" width="8" height="6" fill="none" stroke="#fff"/><path d="M4 5l4 3 4-3" fill="none" stroke="#fff"/></svg>
    <span style="color:var(--green)">info@harrowgatelumen.com</span>
  </div>
  <div class="contact" style="top:110px;display:flex;gap:8px;align-items:flex-start">
    <svg width="16" height="16"><circle cx="8" cy="8" r="8" fill="#fff"/><path d="M8 3a3 3 0 0 1 3 3c0 2-3 6-3 6S5 8 5 6a3 3 0 0 1 3-3z" fill="var(--navy)"/></svg>
    <span><b style="font-weight:600">Meridian Works Harrowgate<br>Lumen Advisors</b><br>410 Calder Ave<br>Suite 220<br>Austin TX, 78702</span>
  </div>

  <div class="legal">© 2025 HARROWGATE LUMEN &nbsp;|&nbsp; All Rights Reserved</div>
</footer>

</body>
</html>
```